Poster Design Project

We need a poster design for a "Karaoke Night" at a bar. Should appeal to a young crowd. Graphics should be musically themed.

Should include info:

When: July 29, 2013 from 7PM to 2AM
Where: Halvern's Pub
1/2 Off on draft beer until 9:30PM
Updates

Project Deadline Extended
Reason: Checking on copyright issues

Target Market(s)

U.S. Market ages 21 to 30, upscale and female

Industry/Entity Type

Crowd

Requirements
Must have
• Needs to be 2 by 3 aspect ratio. Must look good at 3 feet tall (render well at high resolution of 8100 by 5400).
Nice to have
• Do something create with the title "Karaoke Night".

```html
<!DOCTYPE html>
<html lang="en">
<head>
<meta charset="utf-8">
<title>Karaoke Night – Halvern's Pub</title>
<link rel="stylesheet" href="https://fonts.googleapis.com/css2?family=League+Gothic&family=Oswald:wght@500&family=Roboto+Condensed:wght@700&display=swap">
<style>
  :root {
    --red-core: #d4170f;
    --red-mid: #a90d09;
    --red-edge: #3b0503;
    --cream: #efe7cf;
    --badge-black: #0d0d0d;
    --badge-red: #ee1c22;
    --white: #ffffff;
    --splash: #f3d6c8;
    --amber-light: #f0a35a;
    --amber: #d9641c;
    --amber-deep: #b8400f;
  }
  html, body {
    margin: 0;
    padding: 0;
    width: 854px;
    height: 1200px;
    overflow: hidden;
    background: var(--red-edge);
  }
  .poster {
    position: relative;
    width: 854px;
    height: 1200px;
    overflow: hidden;
    background:
      radial-gradient(ellipse 62% 58% at 52% 52%, var(--red-core) 0%, var(--red-mid) 62%, var(--red-edge) 100%);
  }
  .hero-visual {
    position: absolute;
    left: 278px;
    top: 470px;
    width: 300px;
    height: 590px;
    border-radius: 16px;
    background: linear-gradient(180deg, var(--splash) 0%, var(--amber-light) 30%, var(--amber) 65%, var(--amber-deep) 100%);
  }
  .headline {
    position: absolute;
    left: 0;
    top: 0;
    width: 854px;
    height: 600px;
  }
  .title {
    font-family: "League Gothic", "Oswald", sans-serif;
    font-size: 412px;
    fill: var(--cream);
  }
  .event-date {
    font-family: "Oswald", sans-serif;
    font-weight: 500;
    fill: var(--cream);
  }
  .date-line { font-size: 68px; }
  .time-line { font-size: 26px; }
  .offer-badge {
    position: absolute;
    left: 499px;
    top: 696px;
    width: 304px;
    height: 304px;
  }
  .offer-badge svg {
    position: absolute;
    inset: 0;
  }
  .offer-text {
    position: absolute;
    inset: 0;
    padding-top: 36px;
    box-sizing: border-box;
    display: flex;
    flex-direction: column;
    align-items: center;
    justify-content: center;
    font-family: "Roboto Condensed", sans-serif;
    font-weight: 700;
    text-transform: uppercase;
    line-height: 1;
  }
  .offer-amount {
    color: var(--badge-red);
    font-size: 56px;
    letter-spacing: 1px;
    margin-bottom: 10px;
  }
  .offer-detail {
    color: var(--white);
    font-size: 32px;
    margin-bottom: 6px;
  }
  .offer-rule {
    width: 170px;
    height: 4px;
    background: var(--white);
    margin-top: 10px;
  }
  .venue {
    position: absolute;
    left: 0;
    width: 854px;
    top: 1100px;
    margin: 0;
    text-align: center;
    font-family: "Oswald", sans-serif;
    font-weight: 500;
    font-size: 20px;
    letter-spacing: 0.28em;
    color: var(--cream);
    text-transform: uppercase;
  }
</style>
</head>
<body>
<main class="poster">
  <div class="hero-visual" role="img" aria-label="Photo of a shot glass of amber beer with a corded microphone plunged into it, splashing and smoking, its black cable curving off to the right"></div>

  <svg class="headline" viewBox="0 0 854 600" width="854" height="600">
    <text class="title" x="76" y="380" textLength="707" lengthAdjust="spacingAndGlyphs">KARAOKE</text>
    <text class="event-date date-line" x="76" y="451" textLength="247" lengthAdjust="spacingAndGlyphs">THURSDAY 29TH</text>
    <text class="event-date date-line" x="76" y="519" textLength="156" lengthAdjust="spacingAndGlyphs">JULY 2013</text>
    <text class="event-date time-line" x="76" y="557" textLength="122" lengthAdjust="spacingAndGlyphs">7PM - 2AM</text>
  </svg>

  <div class="offer-badge">
    <svg viewBox="0 0 304 304" width="304" height="304" aria-hidden="true">
      <polygon fill="var(--badge-black)" points="304,152 286.4,173.2 296.6,199 273.2,213.7 275,241.4 248.2,248.2 241.4,275 213.7,273.2 199,296.6 173.2,286.4 152,304 130.8,286.4 105,296.6 90.3,273.2 62.6,275 55.8,248.2 29,241.4 30.8,213.7 7.4,199 17.6,173.2 0,152 17.6,130.8 7.4,105 30.8,90.3 29,62.6 55.8,55.8 62.6,29 90.3,30.8 105,7.4 130.8,17.6 152,0 173.2,17.6 199,7.4 213.7,30.8 241.4,29 248.2,55.8 275,62.6 273.2,90.3 296.6,105 286.4,130.8"/>
    </svg>
    <div class="offer-text">
      <span class="offer-amount">1/2 Off</span>
      <span class="offer-detail">On Draft Beer</span>
      <span class="offer-detail">Until 9:30PM</span>
      <span class="offer-rule"></span>
    </div>
  </div>

  <p class="venue">Halvern’s Pub</p>
</main>
</body>
</html>
```